RICE AND RUN WALL POSTER

Hi designer,

I would like to create a poster to put on my wall.

My intention is to place a bicycle onto a wall and have these words vinyl stick next to it.

" Life is not a race.
It is a journey
Enjoy each moment. Relax!
Have a bowl of Rice and Run
Make all your dreams come true "

I like traditional fonts - easy to read. See example. This is something I would love.

It will be on a white wall so black text would be ok. I have also attached my logo - maybe try include Rice and Run font in your design if possible - but not important.

Good luck everyone.

Font styles to use
Decorative
Script

Requirements
Must have
• The placement of my bike will be on the top left corner of the wall so I think it will be best fit if all designs are done in horizontal rectangular shape (landscape)

```html
<!DOCTYPE html>
<html lang="en">
<head>
<meta charset="utf-8">
<title>Rice and Run Wall Poster</title>
<link rel="stylesheet" href="https://fonts.googleapis.com/css2?family=Italianno&family=Great+Vibes&display=swap">
<style>
  :root {
    --wall: #ffffff;
    --ink: #111111;
    --accent: #f0902a;
  }
  html, body {
    margin: 0;
    padding: 0;
    overflow: hidden;
    background: var(--wall);
  }
  .poster {
    position: relative;
    width: 1200px;
    height: 496px;
    background: var(--wall);
    overflow: hidden;
    color: var(--ink);
    font-family: "Italianno", cursive;
  }
  .brand {
    position: absolute;
    left: 64px;
    top: 40px;
    display: flex;
    align-items: center;
    gap: 10px;
  }
  .brand-dot {
    width: 44px;
    height: 44px;
    border: 3px solid var(--accent);
    border-radius: 50%;
    box-sizing: border-box;
  }
  .brand-name {
    font-family: "Italianno", cursive;
    font-size: 34px;
    line-height: 1;
    color: var(--ink);
  }
  .bicycle {
    position: absolute;
    left: 60px;
    top: 125px;
    width: 530px;
    height: 340px;
    border-radius: 40px;
    background: radial-gradient(ellipse at center, #2a2a2a 0%, #000000 80%);
  }
  .quote {
    position: absolute;
    inset: 0;
    margin: 0;
  }
  .quote-line {
    position: absolute;
    white-space: nowrap;
    line-height: 1;
    font-size: 44px;
  }
  .mark {
    position: absolute;
    font-family: "Great Vibes", cursive;
    font-size: 70px;
    line-height: 1;
  }
  .mark-open { left: 606px; top: 138px; }
  .mark-close { left: 1076px; top: 368px; }
  .headword {
    font-family: "Great Vibes", cursive;
    font-size: 120px;
    vertical-align: baseline;
  }
  .emphasis {
    font-family: "Great Vibes", cursive;
    font-size: 54px;
  }
  .line-1 { left: 640px; top: 170px; }
  .line-2 { left: 736px; top: 270px; }
  .line-3 { left: 712px; top: 332px; }
  .line-4 { left: 720px; top: 396px; }
</style>
</head>
<body>
  <main class="poster">
    <div class="brand">
      <span class="brand-dot"></span>
      <span class="brand-name">Rice and Run</span>
    </div>

    <div class="bicycle" role="img" aria-label="Black silhouette of a mountain bicycle, side view"></div>

    <blockquote class="quote">
      <span class="mark mark-open">“</span>
      <span class="quote-line line-1"><span class="headword">Life</span> is not a race. It is a journey</span>
      <span class="quote-line line-2">Enjoy each moment. <span class="emphasis">Relax!</span></span>
      <span class="quote-line line-3">Have a bowl of Rice and Run</span>
      <span class="quote-line line-4">Make all your dreams come true</span>
      <span class="mark mark-close">”</span>
    </blockquote>
  </main>
</body>
</html>
```